Web Design for Real Estate Lending business

I need a web design for my real estate private lending business. The name of the business is Velmora Capital Group. I plan on using Wordpress because that platform is the most optimized for SEO, and we will rely heavily on SEO after the website is built.

I want the website to be responsive of course, and have a fresh, professional, and sleek UI.

The 4 main goals of the website will be:
1. Rank in Google for our relevant key words (Los Angeles real estate hard money lending, real estate financing, fix and flip, private lending, etc)
2. Educate them on what our lending platform is capable of.
3. Capture the contact info (email or phone number) of investors & borrowers who are interested
4. Encourage investors and borrowers to contact us directly

This is an example of a similar business's website: https://www.quendlefunding.example/

Here is my business parter's old website:
https://snapshots.example.net/web/20180822043430/http://www.brantolcg.example/

All of the information on that website (2nd link) will apply to our business. You can pull the information from that Brantol CG website and make it look more modern / sleek, similar to the 1st link (but better).

We are not selling anything on the website.

I also attached a business card template. I would like something similar to this but one that looks slightly more corporate / professional. Keep the colors the same though.

```html
<!DOCTYPE html>
<html lang="en">
<head>
<meta charset="utf-8">
<title>Velmora Capital Group – Hard Money Lending</title>
<link href="https://fonts.googleapis.com/css2?family=Poppins:wght@300;400;500;600;700&display=swap" rel="stylesheet">
<style>
:root{
  --blue:#1f5fb0;
  --blue-dark:#16539f;
  --blue-mid:#2f6fc2;
  --blue-light:#7eaae0;
  --slate:#6f86a3;
  --ink:#2b2b2b;
  --text:#555;
  --gray-bg:#f2f2f2;
  --field:#eef3fb;
  --black:#0d0d0d;
  --white:#fff;
}
*{box-sizing:border-box;margin:0;padding:0}
html,body{width:1200px;height:3984px;overflow:hidden}
body{font-family:'Poppins',sans-serif;color:var(--ink);background:var(--white);position:relative}
.abs{position:absolute}
.topbar{top:0;left:0;width:1200px;height:27px;background:var(--black);color:#fff;font-size:12px;display:flex;justify-content:center;align-items:center;gap:10px}
.header{top:27px;left:0;width:1200px;height:81px}
.brand{position:absolute;left:160px;top:18px;display:flex;align-items:center;gap:8px;font-weight:700;color:var(--blue-dark);line-height:1;font-size:26px;white-space:nowrap}
.brand .mark{width:34px;height:34px;background:var(--blue-dark)}
.brand small{display:block;font-size:16px;color:var(--ink);font-weight:700}
.phone{position:absolute;left:662px;top:26px;display:flex;align-items:center;gap:10px;font-size:14px;color:#333}
.phone .dot{width:28px;height:28px;border-radius:50%;background:var(--blue-light);display:flex;align-items:center;justify-content:center}
.btn-out{position:absolute;left:832px;top:20px;width:90px;height:38px;border:1.5px solid var(--blue);color:var(--blue);font-size:13px;display:flex;align-items:center;justify-content:center}
.btn-fill{position:absolute;left:933px;top:20px;width:106px;height:38px;background:var(--blue);color:#fff;font-size:13px;display:flex;align-items:center;justify-content:center}
.nav{top:108px;left:0;width:1200px;height:39px;background:var(--blue-mid);display:flex;align-items:center;padding-left:163px;gap:47px;color:#fff;font-size:12px;text-transform:uppercase}
.hero{top:147px;left:0;width:1200px;height:533px;overflow:hidden}
.hero-photo{position:absolute;inset:0;background:linear-gradient(180deg,#b9c8d6 0%,#8e9aa4 30%,#7a6f63 65%,#5d5650 100%)}
.hero h1{position:absolute;left:642px;top:86px;font-size:46px;line-height:58px;color:#fff;font-weight:700;text-shadow:2px 2px 4px rgba(0,0,0,.5)}
.features{position:absolute;left:649px;top:212px;width:395px;height:89px;background:rgba(40,100,190,.78);display:grid;grid-template-columns:172px 1fr;padding:10px 10px;gap:6px 8px;color:#fff;font-size:12px;font-weight:500;line-height:14px}
.features span{display:flex;gap:10px;align-items:center;white-space:nowrap}
.features span.wrap{white-space:normal}
.features i{width:14px;height:14px;background:#fff;flex:none;transform:rotate(45deg) scale(.8)}
.hero .cta{position:absolute;left:643px;top:324px;width:164px;height:34px;background:var(--blue-mid);color:#fff;font-size:13px;font-weight:600;display:flex;align-items:center;justify-content:center}
.about{top:680px;left:0;width:1200px;height:503px;text-align:center}
.about h2{position:absolute;top:80px;left:0;width:1200px;display:flex;justify-content:center;align-items:center;gap:22px;font-size:34px;color:var(--blue-dark);font-weight:600}
.about h2 .brand-inline{display:flex;align-items:center;gap:8px;font-size:22px;color:var(--blue-dark);font-weight:700;line-height:1;text-align:left}
.about h2 .brand-inline .mark{width:30px;height:30px;background:var(--blue-dark)}
.about h3{position:absolute;top:144px;width:1200px;font-size:17px;font-weight:500}
.about p{position:absolute;top:172px;left:210px;width:780px;font-size:13.5px;line-height:25px;color:var(--text)}
.about .cta{position:absolute;left:509px;top:292px;width:182px;height:38px;border:1.5px solid var(--blue);color:var(--blue-dark);font-size:15px;display:flex;align-items:center;justify-content:center}
.partners{position:absolute;top:365px;left:180px;width:840px;display:flex;justify-content:space-between;align-items:center}
.partners .badge{width:110px;height:36px;background:#d6d6d6;border-radius:4px}
.partners .sep{width:1px;height:36px;background:#bbb}
.services{top:1183px;left:0;width:1200px;height:747px;background:var(--gray-bg);text-align:center}
.services h2{position:absolute;top:65px;width:1200px;font-size:34px;color:var(--blue-dark);font-weight:600}
.services p{position:absolute;top:128px;width:1200px;font-size:17px}
.tile{position:absolute;display:flex;align-items:center;justify-content:center;border-radius:6px;color:#fff;font-size:18px;font-weight:500;line-height:26px;text-align:center}
.t-slate{background:var(--slate)}
.t-light{background:var(--blue-light)}
.t-blue{background:#2160b3}
.cards{top:1930px;left:0;width:1200px;height:606px}
.card{position:absolute;top:0;width:280px;text-align:center}
.card svg{display:block;margin:74px auto 0}
.card h4{margin-top:26px;font-size:14px;font-weight:600;color:var(--blue-mid);letter-spacing:.3px}
.card p{margin:14px auto 0;width:256px;font-size:12px;line-height:23px;color:var(--text)}
.card a{display:inline-block;margin-top:4px;font-size:13px;color:var(--blue-mid)}
.cash{top:2536px;left:0;width:1200px;height:413px;overflow:hidden;text-align:center;color:#fff}
.cash-photo{position:absolute;inset:0;background:linear-gradient(90deg,#5f8fd0,#3f72bb 50%,#5a8dd0)}
.cash h2{position:absolute;top:115px;width:1200px;font-size:34px;font-weight:600}
.cash p{position:absolute;top:166px;left:240px;width:720px;font-size:19px;line-height:34px;font-weight:300}
.cash .cta{position:absolute;left:537px;top:278px;width:126px;height:36px;background:#fff;color:var(--blue-dark);font-size:14px;display:flex;align-items:center;justify-content:center}
.inform{top:2949px;left:0;width:1200px;height:576px;text-align:center}
.inform h2{position:absolute;top:88px;width:1200px;font-size:34px;color:var(--blue-dark);font-weight:600}
.inform .sub{position:absolute;top:148px;width:1200px;font-size:14px;font-weight:500}
.field{position:absolute;height:44px;background:var(--field);display:flex;align-items:center;font-size:13px;color:#555;text-align:left}
.field .ic{width:42px;height:100%;display:flex;align-items:center;justify-content:center;border-right:1px solid #c9d2de}
.field .ic b{width:11px;height:11px;background:#333;display:block}
.field span{padding-left:12px}
.field.msg{align-items:flex-start}
.field.msg .ic{height:82px;align-items:flex-start;padding-top:16px}
.field.msg span{padding-top:10px}
.inform .q{position:absolute;top:426px;width:1200px;font-size:14px;color:#444}
.checks{position:absolute;top:458px;width:1200px;display:flex;justify-content:center;gap:24px;font-size:13px;color:#444}
.checks label{display:flex;align-items:center;gap:8px}
.checks i{width:14px;height:14px;border:1px solid #aaa;display:block}
.checks i.on{border-color:var(--blue);background:radial-gradient(var(--blue) 45%,#fff 50%)}
.inform .submit{position:absolute;left:551px;top:504px;width:98px;height:36px;background:var(--blue);color:#fff;font-size:14px;display:flex;align-items:center;justify-content:center}
.footer{top:3525px;left:0;width:1200px;height:410px;background:var(--gray-bg)}
.footer svg{position:absolute;left:0;top:0}
.fcol{position:absolute;top:212px;font-size:12.5px;color:#444}
.fcol h5{font-size:15px;font-weight:500;color:var(--ink);margin-bottom:14px}
.links{display:grid;grid-template-columns:116px 200px;row-gap:11px;white-space:nowrap}
.contact li{list-style:none;display:flex;gap:10px;margin-bottom:10px;line-height:18px}
.contact li b{width:9px;height:9px;margin-top:4px;background:var(--blue);border-radius:50%;flex:none}
.fbrand{position:absolute;left:786px;top:212px;width:260px}
.fbrand .brand-inline{display:flex;align-items:center;gap:8px;font-size:26px;font-weight:700;color:var(--blue-dark);line-height:1.05;white-space:nowrap}
.fbrand .brand-inline .mark{width:56px;height:56px;background:var(--blue-dark);flex:none}
.fbrand p{margin-top:14px;font-size:12px;line-height:19px;color:#444}
.follow{margin-top:10px;display:flex;align-items:center;gap:10px;font-size:12.5px}
.follow i{width:27px;height:27px;border-radius:50%;background:var(--blue);display:block}
.follow i.l{background:var(--blue-light)}
.follow i.g{background:#7e93b0}
.copy{top:3935px;left:0;width:1200px;height:49px;background:var(--black);color:#ddd;font-size:13px;display:flex;align-items:center;justify-content:center}
.copy b{color:#fff;font-weight:500;margin:0 4px}
</style>
</head>
<body>

<div class="abs topbar">Los Angeles Real Estate Hard Money Lending <span>|</span> Real Estate Financing <span>|</span> Fix And Flip <span>|</span> Private Lending</div>

<header class="abs header">
  <div class="brand"><span class="mark"></span><div>VELMORA<small>CAPITAL GROUP</small></div></div>
  <div class="phone"><span class="dot"><svg width="14" height="14" viewBox="0 0 24 24"><path fill="#fff" d="M6.6 10.8a15 15 0 006.6 6.6l2.2-2.2c.3-.3.7-.4 1-.2 1.1.4 2.3.6 3.6.6.6 0 1 .4 1 1V20c0 .6-.4 1-1 1A17 17 0 013 4c0-.6.4-1 1-1h3.5c.6 0 1 .4 1 1 0 1.3.2 2.5.6 3.6.1.3 0 .7-.2 1z"/></svg></span>(949) 555-0142</div>
  <div class="btn-out">INVESTOR</div>
  <div class="btn-fill">BORROWER</div>
</header>

<nav class="abs nav"><span>Loan Options</span><span>Property Values</span><span>Property Types</span><span>Investors</span><span>Recommended Professionals</span><span>Contact Us</span></nav>

<section class="abs hero">
  <div class="hero-photo" role="img" aria-label="Aerial photo of a waterfront city skyline with high-rise towers"></div>
  <svg width="1200" height="533" viewBox="0 0 1200 533" style="position:absolute;left:0;top:0">
    <polygon points="0,395 1200,330 1200,533 0,533" fill="#fff"/>
    <polygon points="700,533 1200,330 1200,390" fill="#1f5fb0"/>
    <polygon points="0,395 310,533 0,533" fill="#7eaae0"/>
    <polygon points="310,533 1200,390 1200,533" fill="#fff"/>
  </svg>
  <h1>HARD MONEY<br>LENDING</h1>
  <div class="features">
    <span><i></i>No Hassle Process</span><span><i></i>We Work With All Credit</span>
    <span><i></i>Quick Qualify</span><span class="wrap"><i></i>We'll Get You What You Need</span>
  </div>
  <div class="cta">CONTACT US TODAY</div>
</section>

<section class="abs about">
  <h2>ABOUT <span class="brand-inline"><span class="mark"></span><span>VELMORA<br><small style="font-size:14px">CAPITAL GROUP</small></span></span></h2>
  <h3>Your Fast and Reliable Hard Money Specialists</h3>
  <p>Do you need hard money in hurry to purchase investment property,build your dream home or quick cash? When banks say no, Velmora Capital Group says YES!<br>Welcome to Velmora Capital Group. With more than 100 years combined experience our trained professionals have the knowledge and expertise to customize a loan specific to your needs. We are a private lender.</p>
  <div class="cta">CONTACT US TODAY</div>
  <div class="partners">
    <span class="badge"></span><span class="sep"></span><span class="badge"></span><span class="sep"></span><span class="badge"></span><span class="sep"></span><span class="badge"></span><span class="sep"></span><span class="badge"></span>
  </div>
</section>

<section class="abs services">
  <h2>OUR SERVICES</h2>
  <p>Some Types of Real Estate / Property to serve as Collateral Include</p>
  <div class="tile t-slate" style="left:480px;top:195px;width:240px;height:84px">Office<br>Buildings</div>
  <div class="tile t-slate" style="left:480px;top:287px;width:116px;height:150px">Retail<br>Centers</div>
  <div class="tile t-slate" style="left:604px;top:287px;width:116px;height:150px">Industrial<br>Properties</div>
  <div class="tile t-light" style="left:358px;top:455px;width:240px;height:84px">Multi-Family<br>Apartments</div>
  <div class="tile t-light" style="left:358px;top:547px;width:116px;height:112px">Mobile<br>Home<br>Parks</div>
  <div class="tile t-light" style="left:482px;top:547px;width:116px;height:112px">Self<br>Storages</div>
  <div class="tile t-blue" style="left:606px;top:455px;width:240px;height:84px">Hospitality<br>Properties</div>
  <div class="tile t-blue" style="left:606px;top:547px;width:116px;height:112px">Condo<br>Units</div>
  <div class="tile t-blue" style="left:730px;top:547px;width:116px;height:112px">Assisted<br>Living<br>Condos</div>
</section>

<section class="abs cards">
  <div class="card" style="left:158px">
    <svg width="226" height="250" viewBox="0 0 226 250" role="img" aria-label="Photo of a stressed man at a desk surrounded by paperwork">
      <defs><linearGradient id="g1" x1="0" y1="0" x2="0" y2="1"><stop offset="0" stop-color="#dfe6ee"/><stop offset="1" stop-color="#b7c2cf"/></linearGradient></defs>
      <polygon points="113,2 222,64 222,188 113,248 4,188 4,64" fill="url(#g1)" stroke="#fff" stroke-width="3"/>
    </svg>
    <h4>BILLS PILING UP?</h4>
    <p>With Velmora Capital Group, you'll be back on top of your mountain of paperwork instead of buried underneath it! Let the experienced team members here help consolidate your debt.</p>
    <a><u>Debt Consolidation</u> &rsaquo;</a>
  </div>
  <div class="card" style="left:463px">
    <svg width="226" height="250" viewBox="0 0 226 250" role="img" aria-label="Photo of two builders in hard hats reviewing plans">
      <defs><linearGradient id="g2" x1="0" y1="0" x2="0" y2="1"><stop offset="0" stop-color="#9a9590"/><stop offset="1" stop-color="#5f5a57"/></linearGradient></defs>
      <polygon points="113,2 222,64 222,188 113,248 4,188 4,64" fill="url(#g2)" stroke="#fff" stroke-width="3"/>
    </svg>
    <h4>FINANCE YOUR PROJECT</h4>
    <p>Building a new property? Expanding an operation? Not sure what kind of funding you need? Velmora Capital Group will help you get the funds you need to get the project done!</p>
    <a><u>Ask A Private Lender</u> &rsaquo;</a>
  </div>
  <div class="card" style="left:757px">
    <svg width="226" height="250" viewBox="0 0 226 250" role="img" aria-label="Photo of a business handshake">
      <defs><linearGradient id="g3" x1="0" y1="0" x2="1" y2="0"><stop offset="0" stop-color="#3d4652"/><stop offset=".5" stop-color="#c9a48a"/><stop offset="1" stop-color="#e8ecf1"/></linearGradient></defs>
      <polygon points="113,2 222,64 222,188 113,248 4,188 4,64" fill="url(#g3)" stroke="#fff" stroke-width="3"/>
    </svg>
    <h4>RECOMMENDED PROFESSIONALS</h4>
    <p>These are individuals and companies that Velmora Capital Group works with and trust to provide you with the same level of service you have come to expect here over the years.</p>
    <a><u>See Who Is Recommended!</u> &rsaquo;</a>
  </div>
</section>

<section class="abs cash">
  <div class="cash-photo" role="img" aria-label="Blue-tinted photo of two businessmen meeting at a table with a laptop"></div>
  <h2>GET CASH NOW!</h2>
  <p>Get FREE advice from one of the experienced professionals here regarding any Private Money Loan related topics. It's quick, it's easy, and/or the more questions you answer + the more accurate your results.</p>
  <div class="cta">GET STARTED</div>
</section>

<section class="abs inform">
  <h2>STAY INFORMED</h2>
  <div class="sub">Lorem ipsum dolor sit amet consectetuer adipiscing elit</div>
  <div class="field" style="left:260px;top:180px;width:330px"><span class="ic"><b></b></span><span>Email*</span></div>
  <div class="field" style="left:608px;top:180px;width:330px"><span class="ic"><b></b></span><span>Name*</span></div>
  <div class="field" style="left:260px;top:240px;width:330px"><span class="ic"><b></b></span><span>Company*</span></div>
  <div class="field" style="left:608px;top:240px;width:330px"><span class="ic"><b></b></span><span>Job Title</span></div>
  <div class="field msg" style="left:260px;top:301px;width:678px;height:82px"><span class="ic"><b></b></span><span>Message*</span></div>
  <div class="q">What information are you most interested in? (Select all that apply)</div>
  <div class="checks"><label><i class="on"></i>Investor Newsletter</label><label><i></i>Borrower Newsletter</label></div>
  <div class="submit">SUBMIT</div>
</section>

<footer class="abs footer">
  <svg width="1200" height="200" viewBox="0 0 1200 200">
    <rect width="1200" height="200" fill="#fff"/>
    <polygon points="0,200 890,0 1200,200" fill="#f2f2f2"/>
    <polygon points="0,175 890,0 0,200" fill="#16539f"/>
    <polygon points="890,0 1200,75 1200,160" fill="#7eaae0"/>
  </svg>
  <div class="fcol" style="left:162px">
    <h5>QUICK LINKS</h5>
    <div class="links"><span>Home</span><span>Property Types</span><span>About</span><span>Local Resources</span><span>Glossary</span><span>Recommended Professionals</span><span>Checklists</span><span>Privacy Policy</span><span>Property Values</span><span>Terms of Use</span></div>
  </div>
  <div class="fcol contact" style="left:511px">
    <h5>CONTACT DETAILS</h5>
    <ul>
      <li><b></b><span>418 Harborview Ln<br>Newport Beach, CA. 92660</span></li>
      <li><b></b><span>Call Us<br>(949) 555-0142</span></li>
      <li><b></b><span>Mail Us<br>info@velmora.example</span></li>
    </ul>
  </div>
  <div class="fbrand">
    <div class="brand-inline"><span class="mark"></span><span>VELMORA<br>CAPITAL GROUP</span></div>
    <p>Lorem ipsum dolor sit ame consectetuer adipiscing elit sed diam. Lorem ipsum dolor sit ame consectetuer...</p>
    <div class="follow">Folllow Us <i></i><i class="l"></i><i class="g"></i></div>
  </div>
</footer>

<div class="abs copy">Copyright © 2021 <b>Velmora Capital Group.</b> All Rights Reserved.</div>

</body>
</html>
```